Welland Dental, P.C. New stationary and business card for modern Dental Office

We need a new stationary/envelope/business card design using our newly designed logo. We are looking for an upscale look. Our new logo is used on our signage, using black as the background and white for the lettering. We would like the stationary to have black, white, possible greys or silver. We are looking for a letterhead, envelope, and business card design for three different employees, as well as a 4th card, same design, but just general with no employee name.
Updates

Project Deadline Extended
Reason: We began this project in the middle of our move into our new office. Things got pretty hectic and we just didn't have the time to go through designs. We now settled in and finally eliminated the designs that didn't work for us. We would like to extend the project another 5 days, and then finalize our decision. Most of the submissions showed business cards alone, with no stationary designs. Our original request was for stationary and business cards. Please keep this in mind.

Target Market(s)

Dental patients expecting high quality, cosmetic dentistry

Industry/Entity Type

Business

Contact Information for Business Card

Will need a design using our logo. All cards will be the same, other than that one card will have Office Managers name, One for the Doctor, Hygienist,
1. Office Manager - Marisol Penrose
2. Hygienist - Courtney Whitlock
3. Owen T. Welland, D.D.S.
4. One general one with no staff names

Font styles to use
Other font styles liked:
• see upload

Colors
000000
1b1b1b
757575
c9c9c9
e8e8e8
ffffff

Requirements
Must have
• -Logo
• -Phone number (718)555-0143
• -Address: 4392 63rd Ave
• Lower Level
• Brooklyn, NY 11398

```html
<!DOCTYPE html>
<html lang="en">
<head>
<meta charset="utf-8">
<title>Welland Dental, P.C. — Stationery</title>
<link href="https://fonts.googleapis.com/css2?family=Lato:wght@300;400;700&display=swap" rel="stylesheet">
<style>
  :root {
    --backdrop: #bbbcbe;
    --paper: #ffffff;
    --band: #3d3331;
    --band-edge: #d9d2cc;
    --logo-name: #c9bfb8;
    --logo-dot: #3d3331;
    --logo-faint: #e4e0dd;
    --dot-faint: #cfcbc8;
    --ink-light: #ffffff;
  }
  html, body {
    margin: 0;
    padding: 0;
    width: 1200px;
    height: 927px;
    overflow: hidden;
    background: var(--backdrop);
    font-family: "Lato", sans-serif;
  }
  .canvas {
    position: relative;
    width: 1200px;
    height: 927px;
  }
  .sheet {
    position: absolute;
    background: var(--paper);
    filter: drop-shadow(8px 8px 7px rgba(0,0,0,0.35));
  }
  .sheet svg { display: block; }
  .letterhead { left: 39px; top: 117px; width: 538px; height: 694px; }
  .envelope-back { left: 614px; top: 294px; width: 546px; height: 247px; }
  .envelope-front { left: 613px; top: 563px; width: 548px; height: 247px; }
  .brand-name {
    font-family: "Lato", sans-serif;
    font-weight: 700;
    fill: var(--logo-name);
  }
  .brand-name.faint { fill: var(--logo-faint); }
  .contact-phone {
    font-family: "Lato", sans-serif;
    font-weight: 300;
    font-size: 13px;
    fill: var(--ink-light);
  }
  .contact-address {
    font-family: "Lato", sans-serif;
    font-weight: 700;
    font-size: 13.5px;
    fill: var(--ink-light);
  }
</style>
</head>
<body>
<main class="canvas">

  <section class="sheet letterhead" aria-label="Letterhead">
    <svg width="538" height="694" viewBox="0 0 538 694">
      <rect class="paper" width="538" height="694" fill="var(--paper)"/>
      <g class="brand">
        <text class="brand-name" x="22" y="72" font-size="16">Welland Dental, P.C.</text>
        <circle class="brand-dot" cx="184" cy="66" r="4" fill="var(--logo-dot)"/>
      </g>
      <polygon class="band-edge" points="0,609 538,681 538,694 0,694" fill="var(--band-edge)"/>
      <polygon class="band" points="0,614 538,685 538,694 0,694" fill="var(--band)"/>
      <text class="contact-phone" x="22" y="662">P: (718)555-0143</text>
      <text class="contact-address" x="22" y="680">A: 4392 63rd Ave Lower Level Brooklyn, NY 11398</text>
    </svg>
  </section>

  <section class="sheet envelope-back" aria-label="Envelope, back">
    <svg width="546" height="247" viewBox="0 0 546 247">
      <rect class="paper" width="546" height="247" fill="var(--paper)"/>
      <polygon class="flap" points="0,0 546,0 520,34 24,34" fill="var(--band)"/>
      <g class="brand">
        <text class="brand-name" x="336" y="128" font-size="16">Welland Dental, P.C.</text>
        <circle class="brand-dot" cx="498" cy="122" r="4" fill="var(--logo-dot)"/>
      </g>
      <polygon class="band-edge" points="0,162 546,234 546,247 0,247" fill="var(--band-edge)"/>
      <polygon class="band" points="0,168 546,239 546,247 0,247" fill="var(--band)"/>
      <text class="contact-phone" x="21" y="214">P: (718)555-0143</text>
      <text class="contact-address" x="21" y="232">A: 4392 63rd Ave Lower Level Brooklyn, NY 11398</text>
    </svg>
  </section>

  <section class="sheet envelope-front" aria-label="Envelope, front">
    <svg width="548" height="247" viewBox="0 0 548 247">
      <rect class="paper" width="548" height="247" fill="var(--paper)"/>
      <g class="brand">
        <text class="brand-name faint" x="176" y="128" font-size="19">Welland Dental, P.C.</text>
        <circle class="brand-dot" cx="369" cy="121" r="5" fill="var(--dot-faint)"/>
      </g>
    </svg>
  </section>

</main>
</body>
</html>
```